velmoragems.com.au needs a new web design!

We are after a refurbished web design. velmoragems.com.au is an online jewellery store - it represents a brand that is elegant, graceful and superior in quality.

We have colours that we like but are open to new colour schemes. Our favourite colours are teal and cherry (see attached colour story). We also like simple designs with lots of white space.

A website which we love the layout and design is www.brasková.com.au please try and design in a similar fashion.

We require three important pages:

- Home page
- Tiled product category Page (eg. earrings, see current website)
- Single Product Page.

Please be aware we are limited to the current Content Management System for our website so using similiar (but not limited too) layout would be helpful for the lonely developer (me).

Our designer should provide (at least) photoshop files for our disposal with category headings etc being able to be edited as we add or change new product categories.

We have plans to get large photos of models for the home page in the future, but should also be available for large photos of jewellery. Basically we believe photos are essential to sell our product, so please don't be afraid to incorporate some dummy photos into your design. Especially the home page!

We also offer free shipping Australia Wide, please incorporate this into the home page, product and category pages, it needs to show the visitor that it is specifically Free Australian wide shipping.

Other stuff we need:

A cool shipping info button/box (see current single product page)
Some Social networking buttons/boxes for Pinbrook and chirpel for possible use on home page.

please email oliver@velmoragems.com.au if you have any questions.

Many thanks and we look forward to reviewing your designs.
Updates

Thankyou all for your designs, I have messaged 4 designs which are the front runners. some have been reuqested to make slight adjustments, others have been asked to submit the other pages as per brief.

Cheers,

Oliver

Target Market(s)

Ladies in Australia between the ages of 25 and 55

Industry/Entity Type

Shipping

Requirements
Must have
• Hovers, actions and transitions and potential drop downs
Should not have
• Korvix glint.

```html
<!DOCTYPE html>
<html lang="en">
<head>
<meta charset="utf-8">
<title>velmoragems — Home</title>
<link rel="stylesheet" href="https://fonts.googleapis.com/css2?family=PT+Sans:wght@400;700&family=Delius&family=Arimo:wght@400;700&display=swap">
<style>
  :root {
    --teal: #2a9688;
    --teal-dark: #237f73;
    --cherry: #a8102e;
    --cherry-light: #e0455a;
    --band: #f1f0ea;
    --band-line: #e4e3dc;
    --ink: #2b2b2b;
    --muted: #4a4a55;
    --cart-green: #6aaa1c;
    --white: #ffffff;
  }
  * { box-sizing: border-box; margin: 0; padding: 0; }
  html, body { width: 1200px; height: 925px; overflow: hidden; background: var(--white); }
  body { position: relative; font-family: "PT Sans", sans-serif; color: var(--ink); }
  a { color: inherit; text-decoration: none; transition: color .2s ease, background-color .2s ease, transform .2s ease; }

  .top-band {
    position: absolute; left: 0; top: 30px; width: 1200px; height: 44px;
    background: var(--band);
    border-top: 2px solid var(--band-line); border-bottom: 2px solid var(--band-line);
  }
  .brand {
    position: absolute; left: 82px; top: 6px; width: 172px; height: 142px;
    border: 1.5px solid #bfded8; border-radius: 50%; background: var(--white);
    display: flex; align-items: center; justify-content: center;
    font-family: "PT Sans", sans-serif; font-size: 20px; font-weight: 400; color: var(--cherry);
    z-index: 3;
  }
  .top-nav { position: absolute; top: 43px; left: 626px; display: flex; gap: 22px; font-size: 15px; }
  .top-nav a { display: flex; align-items: center; gap: 8px; }
  .top-nav a::before { content: ""; width: 7px; height: 10px; border-radius: 50%; background: var(--teal); }
  .top-nav a:hover { color: var(--teal); }
  .cart { position: absolute; left: 868px; top: 38px; display: flex; align-items: center; gap: 6px; color: var(--cart-green); font-size: 15px; }
  .cart small { font-size: 12px; }
  .cart b { color: var(--ink); }
  .shipping-note {
    position: absolute; right: 66px; top: 88px;
    font-size: 13px; color: var(--teal); display: flex; align-items: center; gap: 6px;
  }
  .shipping-note::before { content: ""; width: 8px; height: 8px; background: var(--cherry); }

  .category-menu { position: absolute; left: 0; top: 0; list-style: none; }
  .category-menu a {
    position: absolute; height: 46px; display: flex; align-items: center;
    background: var(--teal); color: #1d2a28; font-size: 21px;
    border-radius: 14px 0 0 14px; padding-left: 44px;
  }
  .category-menu a::before { content: "❯"; position: absolute; left: 44px; color: var(--white); font-size: 15px; }
  .category-menu a span { margin-left: 28px; }
  .category-menu a:hover { background: var(--teal-dark); color: var(--white); transform: translateX(-6px); }
  .category-menu .is-active { left: 243px; top: 302px; width: 140px; color: var(--white); padding-left: 24px; }
  .category-menu .is-active::before { left: auto; right: 30px; }
  .category-menu .is-active span { margin-left: 0; }

  .hero { position: absolute; left: 333px; top: 131px; width: 690px; height: 578px; z-index: 2; }
  .hero-title { position: absolute; left: 170px; top: 54px; color: var(--white); font-family: "Delius", cursive; font-size: 40px; font-weight: 400; white-space: nowrap; }
  .hero-title small { font-family: "PT Sans", sans-serif; font-size: 18px; font-weight: 400; color: #f2e6e8; }
  .slider-dots { position: absolute; left: 293px; top: 536px; display: flex; gap: 7px; }
  .slider-dots a { width: 27px; height: 20px; border-radius: 50%; background: var(--teal); display: flex; align-items: center; justify-content: center; }
  .slider-dots a:hover { background: var(--teal-dark); }
  .slider-dots .is-current::after { content: ""; width: 8px; height: 8px; border-radius: 50%; background: var(--white); }

  .footer-band {
    position: absolute; left: 0; top: 760px; width: 1200px; height: 46px;
    background: var(--band); border-top: 2px solid var(--band-line); border-bottom: 2px solid var(--band-line);
    font-family: "Arimo", sans-serif; font-size: 12px; color: var(--muted);
  }
  .footer-links { position: absolute; left: 404px; top: 14px; display: flex; gap: 12px; }
  .footer-links a:hover { color: var(--teal); }
  .sep { color: #6d8fc4; }
  .sep.warm { color: #e08a3c; }
  .social { position: absolute; right: 40px; top: 15px; display: flex; gap: 8px; font-size: 11px; white-space: nowrap; }
  .social a { display: flex; align-items: center; gap: 3px; }
  .social a::before { content: ""; width: 8px; height: 8px; background: var(--teal); }
  .social a:hover { color: var(--cherry); }

  .copyright { position: absolute; top: 826px; left: 420px; font-family: "Arimo", sans-serif; font-size: 12px; color: var(--muted); display: flex; gap: 14px; }
  .copyright a { color: var(--cherry-light); font-weight: 700; }
  .copyright .sep { color: var(--cherry-light); }
  .rule { position: absolute; left: 0; top: 857px; width: 1200px; height: 1px; background: var(--band-line); }
  .payments { position: absolute; top: 877px; left: 560px; display: flex; gap: 12px; font-family: "Arimo", sans-serif; font-size: 15px; font-weight: 700; color: #1f3d7a; }
</style>
</head>
<body>
  <header>
    <div class="top-band"></div>
    <a class="brand" href="#">velmoragems</a>
    <nav class="top-nav">
      <a href="#">About</a>
      <a href="#">Customer Service</a>
    </nav>
    <a class="cart" href="#">
      <svg width="38" height="30" viewBox="0 0 38 30" aria-hidden="true">
        <path d="M2 4h6l4 16h20l4-12H10" fill="none" stroke="#6aaa1c" stroke-width="3" stroke-linejoin="round"/>
        <circle cx="14" cy="25" r="3" fill="#6aaa1c"/><circle cx="29" cy="25" r="3" fill="#6aaa1c"/>
      </svg>
      Shopping Cart <small>now in your cart <b>0</b> items</small>
    </a>
    <p class="shipping-note">Free shipping Australia-wide</p>
  </header>

  <nav>
    <ul class="category-menu">
      <li><a class="is-active" href="#"><span>Chains</span></a></li>
      <li><a href="#" style="left:124px;top:359px;width:280px"><span>Earrings</span></a></li>
      <li><a href="#" style="left:124px;top:417px;width:280px"><span>Bracelets</span></a></li>
      <li><a href="#" style="left:124px;top:473px;width:280px"><span>Necklaces</span></a></li>
      <li><a href="#" style="left:126px;top:531px;width:280px"><span>&nbsp;Pendants</span></a></li>
    </ul>
  </nav>

  <main class="hero">
    <svg width="690" height="578" viewBox="0 0 690 578">
      <defs>
        <radialGradient id="photoTone" cx="45%" cy="45%" r="65%">
          <stop offset="0" stop-color="#f4f4f4"/><stop offset=".7" stop-color="#dcdcdc"/><stop offset="1" stop-color="#bdbdbd"/>
        </radialGradient>
        <clipPath id="belowBand"><rect x="0" y="115" width="690" height="470"/></clipPath>
      </defs>
      <ellipse cx="345" cy="289" rx="345" ry="289" fill="var(--cherry)"/>
      <ellipse cx="345" cy="317" rx="296" ry="207" fill="url(#photoTone)" clip-path="url(#belowBand)"
               role="img" aria-label="Photo of silver bangles, rings and chain bracelets on a white surface"/>
    </svg>
    <h1 class="hero-title">welcome <small>to velmoragems.</small></h1>
    <div class="slider-dots">
      <a class="is-current" href="#" aria-label="Slide 1"></a>
      <a href="#" aria-label="Slide 2"></a>
      <a href="#" aria-label="Slide 3"></a>
      <a href="#" aria-label="Slide 4"></a>
    </div>
  </main>

  <footer>
    <div class="footer-band">
      <div class="footer-links">
        <a href="#">Specials</a><span class="sep">|</span>
        <a href="#">Advanced Search</a><span class="sep">|</span>
        <a href="#">Reviews</a><span class="sep warm">|</span>
        <a href="#">Create an Account</a><span class="sep">|</span>
        <a href="#">Log In</a>
      </div>
      <div class="social">
        <a href="#">Feed</a><a href="#">Pinbrook</a><a href="#">Linkora</a><a href="#">chirpel</a>
      </div>
    </div>
    <p class="copyright">Copyright © 2012 Jewelry Store <a href="#">Privacy Notice</a><span class="sep">|</span><a href="#">Conditions of Use</a></p>
    <div class="rule"></div>
    <div class="payments"><span>Paywell</span><span>Vistra</span></div>
  </footer>
</body>
</html>
```